Business Card for Professional Domainer

Require a business card design for an Individual Person who is a Professional Domainer.

Who is a Professional Domainer?
A domainer is someone who earns a profit buying and selling domain names.
Professional Domainer are the ones who do this on a full time basis.

So we require the business card design to be related to the above work.

There is no company or any logo currently, as the card is required for an Individual Person.

Business Card required to mention following details:

1. Full Name of the Person (Ex: Marisol Kettner)
2. Education Qualification (Ex: B.Tech Computer Science)
3. Mobile Number (Ex: +71 4837160295)
4. Website (Ex: www.trelmixo.com)
5. Email (Ex: hello@trelmixo.com)

Positioning of the details:

1. Mobile Number should be placed to Right Top Corner
2. Education Qualification should be just below Full Name
3. Website and Email should be on Bottom Part, on a bar at the bottom

It's important to include images related to the nature of work (Domaining) in the card design.
A good related image would be great. Image should be either in background or as a logo.
The image should be focus of the business card, and shoudl speak out on itself.
Anyone looking at the card should understand at one look what work is being done.
So kindly use images in the design which are highly relevant to domaining and domain names.

Along with the image, it's also good if you use the word "Professional Domainer" anywhere in the design.
Maybe along with the image or somewhere it would fit. These words would be like company name.
So please try to use these words "Professional Domainer" in the design, as it will help a lot.

Colors: Blue, Red, Green

We like these colors, but you are free to use any color which would be good for the design.

Card design should be according to Quornalex specs:

Document Trim Size = 91 x 55 mm | 1075 x 650 pixels
Full Bleed Size = 94 x 58 mm | 1110 x 685 pixels

Last thing, the business card should look professional and clean.
People should know that the person is a Professional Domainer at one look of the card.

Thank You and All the Best :)

Message to the the designers working on this project:

We have now guaranteed this project. This means, we will 100% choose a design and award the project to the one we like the best. So kindly submit your best designs before Wednesday, 3 July 2013. After that we are going to finalize the project and award to the best one. So please hurry up so that you are not too late. Thank You and All the Best!

```html
<!DOCTYPE html>
<html lang="en">
<head>
<meta charset="utf-8">
<title>Professional Domainer – Business Card</title>
<link rel="stylesheet" href="https://fonts.googleapis.com/css2?family=Didact+Gothic&family=Roboto:wght@700&display=swap">
<style>
  :root {
    --page-bg: #1a1a1c;
    --card-deep: #0b2530;
    --card-mid: #17596b;
    --card-glow: #2a8097;
    --frame: #5f98aa;
    --bar-bg: #6aa2b4;
    --bar-ink: #17323b;
    --text-light: #f1f6f8;
    --text-soft: #d3e2e7;
    --photo-dark: #0c0f12;
    --photo-skin: #c79a80;
  }
  * { margin: 0; padding: 0; box-sizing: border-box; }
  html, body { width: 1200px; height: 942px; overflow: hidden; background: var(--page-bg); }
  .canvas { position: relative; width: 1200px; height: 942px; }

  .card {
    position: absolute; left: 62px; top: 146px; width: 1075px; height: 650px;
    overflow: hidden;
    background: radial-gradient(ellipse at 70% 45%, var(--card-glow) 0%, var(--card-mid) 40%, var(--card-deep) 100%);
  }

  .hero-photo {
    position: absolute; left: 0; top: 0; width: 560px; height: 650px;
    background:
      radial-gradient(ellipse 170px 90px at 430px 330px, var(--photo-skin) 0%, rgba(199,154,128,0) 100%),
      linear-gradient(100deg, var(--photo-dark) 0%, #15191d 55%, rgba(23,89,107,0) 100%);
  }
  .network-glow {
    position: absolute; inset: 0;
    background:
      radial-gradient(circle at 62% 28%, rgba(255,255,255,.18) 0, rgba(255,255,255,0) 120px),
      radial-gradient(circle at 88% 72%, rgba(255,255,255,.12) 0, rgba(255,255,255,0) 150px);
  }

  .frame-lines { position: absolute; inset: 0; }

  .title-box {
    position: absolute; left: 600px; top: 44px; width: 440px;
    color: var(--text-soft); font-family: "Didact Gothic", sans-serif;
    font-size: 60px; line-height: 1.05; text-align: left;
  }
  .title-box .line-two { display: block; padding-left: 40px; }

  .identity {
    position: absolute; left: 46px; top: 360px;
    font-family: "Didact Gothic", sans-serif; color: var(--text-light);
  }
  .identity .name { font-size: 70px; font-weight: 400; letter-spacing: .5px; }
  .identity .qualification { font-size: 36px; color: var(--text-soft); margin-top: 6px; }

  .phone {
    position: absolute; right: 34px; top: 300px;
    font-family: "Roboto", sans-serif; font-weight: 700; font-size: 40px;
    color: var(--text-light); letter-spacing: 1px;
  }

  .contact-bar {
    position: absolute; left: 0; bottom: 0; width: 1075px; height: 86px;
    background: var(--bar-bg);
    display: flex; align-items: center; justify-content: space-around;
    font-family: "Roboto", sans-serif; font-weight: 700; font-size: 30px;
    color: var(--bar-ink); letter-spacing: .5px;
  }
</style>
</head>
<body>
<div class="canvas">
  <div class="card">
    <div class="hero-photo" role="img" aria-label="Photo of a person in a dark suit pointing a finger at a glowing network of connected points"></div>
    <div class="network-glow" role="img" aria-label="Soft glow of a connected-dots network pattern across the teal background"></div>

    <svg class="frame-lines" width="1075" height="650" viewBox="0 0 1075 650" aria-hidden="true">
      <rect x="560" y="0" width="10" height="564" fill="var(--frame)"/>
      <rect x="560" y="18" width="515" height="8" fill="var(--frame)"/>
      <rect x="560" y="250" width="515" height="6" fill="var(--frame)" opacity=".8"/>
    </svg>

    <div class="title-box">
      <span class="line-one">Professional</span>
      <span class="line-two">Domainer</span>
    </div>

    <div class="phone">+71 4837160295</div>

    <div class="identity">
      <div class="name">Marisol Kettner</div>
      <div class="qualification">B.Tech Computer Science</div>
    </div>

    <div class="contact-bar">
      <span class="website">www.trelmixo.com</span>
      <span class="email">hello@trelmixo.com</span>
    </div>
  </div>
</div>
</body>
</html>
```